hi all

Im after a new age looking business card with my company logo on it

must include these details, I would like the PH and Email to be symbols

If the colours used for card could be kept within the colours used in logo that I have supplied that would be great, if another colour is to be used dark grey would be ok. no light bulbs etc thanks

Details below to be incorporated on card

Damian Holloway

Lic E871302

PH 0219647381

E info@brightvaleelectrical.example.nz

Domestic Commercial Industrial Electricians

```html
<!DOCTYPE html>
<html lang="en">
<head>
<meta charset="utf-8">
<title>Brightvale Electrical – Business Card</title>
<link rel="stylesheet" href="https://fonts.googleapis.com/css2?family=Exo+2:wght@500;600&display=swap">
<style>
  :root {
    --white: #ffffff;
    --brand-blue: #1676c4;
    --navy-light: #2c3590;
    --navy: #1f2577;
    --navy-deep: #161a4e;
    --text-light: #f4f6ff;
  }
  * { margin: 0; padding: 0; box-sizing: border-box; }
  html, body {
    width: 1200px;
    height: 720px;
    overflow: hidden;
    background: var(--white);
  }
  .card {
    position: relative;
    width: 1200px;
    height: 720px;
    display: flex;
    font-family: "Exo 2", sans-serif;
  }
  .brand-panel {
    position: relative;
    width: 543px;
    height: 100%;
    background: var(--white);
  }
  .brand-mark {
    position: absolute;
    left: 50%;
    top: 250px;
    width: 104px;
    height: 104px;
    margin-left: -52px;
    border-radius: 50%;
    background: var(--brand-blue);
  }
  .brand-name {
    position: absolute;
    left: 0;
    width: 100%;
    top: 384px;
    text-align: center;
    color: var(--brand-blue);
    font-size: 34px;
    font-weight: 600;
    letter-spacing: 2px;
    text-transform: uppercase;
    line-height: 1;
  }
  .info-panel {
    position: relative;
    flex: 1;
    height: 100%;
    overflow: hidden;
    background: linear-gradient(155deg, var(--navy) 0%, var(--navy-light) 45%, var(--navy) 75%, var(--navy-deep) 100%);
    color: var(--text-light);
  }
  .circuit-glow {
    position: absolute;
    top: -40px;
    right: -40px;
    width: 560px;
    height: 320px;
    background: radial-gradient(circle at 72% 52%, rgba(111, 216, 255, 0.85) 0%, rgba(60, 150, 255, 0.35) 10%, rgba(44, 70, 190, 0.15) 32%, rgba(31, 37, 119, 0) 62%);
  }
  .holder-name {
    position: absolute;
    left: 81px;
    top: 245px;
    font-size: 62px;
    font-weight: 500;
    font-variant: small-caps;
    letter-spacing: 1px;
    line-height: 1;
  }
  .services {
    position: absolute;
    left: 81px;
    top: 342px;
    list-style: none;
    font-size: 31px;
    font-weight: 500;
    font-variant: small-caps;
    line-height: 39px;
    letter-spacing: 0.5px;
  }
  .contact-list {
    position: absolute;
    left: 81px;
    top: 502px;
    list-style: none;
  }
  .contact-item {
    display: flex;
    align-items: center;
    height: 45px;
    font-size: 26px;
    font-weight: 500;
    font-variant: small-caps;
    letter-spacing: 0.5px;
  }
  .contact-item.email { font-size: 22px; }
  .contact-icon {
    width: 30px;
    height: 30px;
    margin-right: 27px;
    flex-shrink: 0;
  }
</style>
</head>
<body>
<div class="card">
  <section class="brand-panel">
    <div class="brand-mark"></div>
    <h1 class="brand-name">Brightvale Electrical</h1>
  </section>

  <section class="info-panel">
    <div class="circuit-glow" role="img" aria-label="Decorative glowing circuit lines and scattered light particles"></div>

    <h2 class="holder-name">Damian Holloway</h2>

    <ul class="services">
      <li>· Domestic · Commercial</li>
      <li>· Industrial Electricians</li>
    </ul>

    <ul class="contact-list">
      <li class="contact-item licence">
        <svg class="contact-icon" viewBox="0 0 30 30" aria-hidden="true">
          <rect x="1" y="6" width="28" height="18" rx="2" fill="#ffffff"/>
          <circle cx="9" cy="13" r="3" fill="#1f2577"/>
          <path d="M4.5 21c0-3 2-4.5 4.5-4.5s4.5 1.5 4.5 4.5z" fill="#1f2577"/>
          <rect x="16" y="10" width="10" height="2" fill="#1f2577"/>
          <rect x="16" y="14" width="10" height="2" fill="#1f2577"/>
          <rect x="16" y="18" width="10" height="2" fill="#1f2577"/>
        </svg>
        <span>Lic E871302</span>
      </li>
      <li class="contact-item phone">
        <svg class="contact-icon" viewBox="0 0 30 30" aria-hidden="true">
          <circle cx="15" cy="15" r="14" fill="#ffffff"/>
          <path d="M10.5 7.5l3 3-1.8 2.2c1 2.2 2.6 3.8 4.8 4.8l2.2-1.8 3 3-1.9 2.6c-5.8-0.6-10.6-5.4-11.2-11.2z" fill="#1f2577"/>
        </svg>
        <span>0219647381</span>
      </li>
      <li class="contact-item email">
        <svg class="contact-icon" viewBox="0 0 30 30" aria-hidden="true">
          <circle cx="15" cy="15" r="14" fill="#ffffff"/>
          <rect x="8" y="10" width="14" height="10" rx="1" fill="none" stroke="#1f2577" stroke-width="1.8"/>
          <path d="M8.5 10.8l6.5 5 6.5-5" fill="none" stroke="#1f2577" stroke-width="1.8"/>
        </svg>
        <span>info@brightvaleelectrical.example.nz</span>
      </li>
    </ul>
  </section>
</div>
</body>
</html>
```